3D Printing Business coming soon page

Hi we are looking for a one page "coming soon" website for our business. The business is called "Solevia Labs" and it is a new solution which 3D Prints Orthotics (Insoles).

The design should include our logo, an improved version of our promotional image (attached), a web form for capturing interest from people, a countdown timer and some text.

Follow the colour scheme which is shown in our logo along with our other colours - Orange (RGB#ff8300) and Light Green (RGB#30f20a)
Updates

Industry/Entity Type

Business

Font styles to use
Sans Serif

Requirements
Must have
• Logo (Attached)
Improved version of Promotional Image
Web Form design for capturing Name, EMail Address and Comments along with a Turin test
Countdown Timer
Text - "Solevia Labs will shake up the Orthotics Industry. Foot Orthosis patient-ready in hours for a fraction of the price you are paying today. Welcome to the new world of 3D Printing!"

```html
<!DOCTYPE html>
<html lang="en">
<head>
<meta charset="utf-8">
<title>Solevia Labs – Coming Soon</title>
<link rel="stylesheet" href="https://fonts.googleapis.com/css2?family=Oswald:wght@300;400;500;700&display=swap">
<style>
  :root {
    --green-bright: #30f20a;
    --green-head: #5aa24a;
    --panel-grey: #666666;
    --navy: #1c3f7c;
    --teal: #1d78a8;
    --label-blue: #1f5f9a;
    --ink: #111111;
    --white: #ffffff;
    --photo-grey: #d6d6d6;
  }
  * { box-sizing: border-box; margin: 0; padding: 0; }
  html, body { width: 1200px; height: 1164px; overflow: hidden; background: var(--white); }
  body { font-family: "Oswald", sans-serif; position: relative; }
  .backdrop {
    position: absolute; inset: 0 0 380px 0;
    background:
      radial-gradient(ellipse 420px 520px at 120px 380px, #e4e4e4 0%, rgba(255,255,255,0) 75%),
      radial-gradient(ellipse 700px 260px at 600px 200px, #efefef 0%, rgba(255,255,255,0) 80%);
  }
  .page-title {
    position: absolute; top: 28px; left: 0; width: 1200px; text-align: center;
    font-weight: 700; font-size: 52px; line-height: 64px; letter-spacing: -1px;
    color: var(--green-bright); text-shadow: 0 3px 3px rgba(0,0,0,.35);
  }
  .countdown { position: absolute; top: 106px; left: 0; width: 1200px; height: 140px; }
  .unit { position: absolute; top: 0; text-align: center; transform: translateX(-50%); }
  .unit-value {
    display: block; font-weight: 500; font-size: 120px; line-height: 112px; letter-spacing: -2px;
    background: linear-gradient(180deg, var(--navy) 0%, var(--teal) 100%);
    -webkit-background-clip: text; background-clip: text; color: transparent;
  }
  .unit-label { display: block; margin-top: 2px; font-weight: 300; font-size: 19px; color: var(--label-blue); }
  .pitch {
    position: absolute; top: 250px; left: 100px; width: 1000px; text-align: center;
    font-weight: 300; font-size: 27px; line-height: 33px; color: var(--ink);
  }
  .contact-panel {
    position: absolute; left: 488px; top: 390px; width: 274px; height: 365px;
    background: var(--panel-grey);
  }
  .contact-head {
    height: 66px; background: var(--green-head); border-bottom: 4px solid #4c8a3e;
    color: var(--white); font-weight: 500; font-size: 28px; line-height: 62px; text-align: center; letter-spacing: 1px;
  }
  .field {
    position: absolute; left: 14px; width: 245px; background: var(--white);
    border: 2px solid #d8d8d8; font-family: "Oswald", sans-serif; font-weight: 300;
    font-size: 11px; letter-spacing: .5px; color: #888; padding: 6px 10px;
  }
  .field-email { top: 78px; height: 29px; }
  .field-message { top: 116px; height: 112px; }
  .captcha {
    position: absolute; left: 45px; top: 239px; width: 183px; height: 70px;
    background: #a32a1a; border-radius: 4px; padding: 3px;
  }
  .captcha-words { height: 36px; background: var(--white); border-radius: 2px; }
  .captcha-entry {
    margin-top: 3px; width: 104px; height: 26px; background: #f5e49a; border-radius: 2px;
    font-size: 7px; font-weight: 500; color: #333; padding: 2px 8px;
  }
  .captcha-entry span { display: block; margin-top: 2px; height: 9px; background: var(--white); }
  .captcha-mark { position: absolute; right: 10px; bottom: 10px; width: 18px; height: 18px; background: var(--white); }
  .submit-btn {
    position: absolute; left: 58px; top: 320px; width: 152px; height: 33px; border: 0;
    background: linear-gradient(180deg, #55f535 0%, var(--green-bright) 100%);
    color: var(--white); font-family: "Oswald", sans-serif; font-weight: 700; font-size: 21px;
  }
  .brand-name {
    position: absolute; left: 470px; top: 812px; width: 260px; text-align: center;
    font-weight: 700; font-size: 44px; line-height: 56px; color: var(--navy);
  }
  .step-label { position: absolute; font-weight: 300; font-size: 18px; color: var(--ink); transform: translateX(-50%); white-space: nowrap; }
  .step-image { position: absolute; border-radius: 4px; }
  .flow-arrows { position: absolute; inset: 0; }
</style>
</head>
<body>
  <div class="backdrop" role="img" aria-label="Faint grey stacked panels decorating the background"></div>

  <h1 class="page-title">Comming Soon</h1>

  <div class="countdown">
    <div class="unit" style="left:360px"><span class="unit-value">000</span><span class="unit-label">Days</span></div>
    <div class="unit" style="left:540px"><span class="unit-value">00</span><span class="unit-label">Hours</span></div>
    <div class="unit" style="left:695px"><span class="unit-value">00</span><span class="unit-label">Minutes</span></div>
    <div class="unit" style="left:850px"><span class="unit-value">00</span><span class="unit-label">Seconds</span></div>
  </div>

  <p class="pitch">Solevia Labs will shake up the Orthotics Industry. Foot Orthosis patient-ready in hours for a fraction of the price you are paying today. Welcome to the new world of 3D Printing!</p>

  <form class="contact-panel">
    <div class="contact-head">CONTACT US</div>
    <div class="field field-email">Email Address</div>
    <div class="field field-message">Text Your Message</div>
    <div class="captcha">
      <div class="captcha-words" role="img" aria-label="Distorted verification words"></div>
      <div class="captcha-entry">Type the two words:<span></span></div>
      <div class="captcha-mark"></div>
    </div>
    <button type="button" class="submit-btn">SUBMIT</button>
  </form>

  <div class="brand-name">Solevia Labs</div>

  <div class="step-label" style="left:186px;top:750px">1. Scan The Foot</div>
  <div class="step-image" role="img" aria-label="Tablet with a 3D scanner attached" style="left:124px;top:774px;width:118px;height:121px;background:linear-gradient(160deg,#f2f2f2,#bdbdbd)"></div>

  <div class="step-label" style="left:1020px;top:750px">4. Fit It</div>
  <div class="step-image" role="img" aria-label="Hands placing a printed insole into a shoe" style="left:947px;top:789px;width:147px;height:84px;background:linear-gradient(160deg,#e6d6c4,#3a3a3a)"></div>

  <div class="step-label" style="left:463px;top:970px">2. Design The Orthotic</div>
  <div class="step-image" role="img" aria-label="Orthotic design software showing a foot model" style="left:385px;top:1002px;width:155px;height:87px;background:linear-gradient(160deg,#f4f4f4,#e7c4b4)"></div>

  <div class="step-label" style="left:778px;top:970px">3. 3D Print</div>
  <div class="step-image" role="img" aria-label="Desktop 3D printer" style="left:714px;top:1002px;width:123px;height:121px;background:linear-gradient(180deg,#b3334f 0%,#9fc7e0 40%,#e9e6df 100%)"></div>

  <svg class="flow-arrows" width="1200" height="1164" viewBox="0 0 1200 1164" aria-hidden="true">
    <polygon points="305,922 287,978 227,975" fill="#30f20a"/>
    <polygon points="609,1007 646,1053 609,1100" fill="#30f20a"/>
    <polygon points="908,968 965,965 983,1021" fill="#30f20a"/>
  </svg>
</body>
</html>
```